DL size Flyer

Design for DL Flyer double sided. One side for blocked drains and pipe relining.
Other side for general plumbing. eg leaking taps, leaking toilets, burst pipes, cctv inspections, gas installations, blocked drains.
Your local plumbing experts.
Relining pictures similar to what we need designed.

Phone number is 0487 312 564 ( on both sides)
Logo for payment methods: cash, quon, cheque. ( on both sides)

Plumbing

```html
<!DOCTYPE html>
<html lang="en">
<head>
<meta charset="utf-8">
<title>Harbourline Plumbing &amp; Drainage – DL Flyer</title>
<link rel="stylesheet" href="https://fonts.googleapis.com/css2?family=Roboto+Condensed:ital,wght@0,400;0,700;0,800;1,700;1,900&family=Lato:wght@400;700&display=swap">
<style>
  :root{
    --page:#d6d6d6;
    --red:#e8333d;
    --red-dark:#c81e2a;
    --blue:#1f74c9;
    --blue-dark:#0f4f9a;
    --cyan:#36c0dc;
    --ink:#151515;
    --paper:#f1f1f1;
    --white:#ffffff;
    --navy:#1b2f6b;
  }
  *{box-sizing:border-box;margin:0;padding:0}
  html,body{width:1200px;height:844px;overflow:hidden}
  body{background:var(--page);font-family:"Lato",sans-serif;position:relative}

  .flyer{position:absolute;top:42px;width:360px;height:760px;background:var(--paper);overflow:hidden;box-shadow:0 2px 8px rgba(0,0,0,.18)}
  .flyer--front{left:205px}
  .flyer--back{left:635px}

  .brand-band{position:absolute;left:0;top:0;width:100%;height:100px;display:flex;flex-direction:column;align-items:center;justify-content:center;color:var(--white);font-family:"Roboto Condensed",sans-serif;font-weight:800;text-transform:uppercase;line-height:1}
  .flyer--front .brand-band{background:var(--red)}
  .flyer--back .brand-band{background:var(--cyan)}
  .brand-name{font-size:38px;letter-spacing:2px}
  .brand-sub{font-size:15px;letter-spacing:4.5px;margin-top:6px}

  .photo{position:absolute}
  .photo--front-tradesman{left:0;top:100px;width:100%;height:200px;background:linear-gradient(135deg,#e9ecef 0%,#9fb3cf 45%,#3d5a8c 70%,#c9852e 100%)}
  .photo--back-pipework{left:0;top:100px;width:100%;height:220px;background:linear-gradient(120deg,#a9ab6a 0%,#c7c8b4 40%,#8c7a62 75%,#d8b59b 100%)}
  .divider{position:absolute;left:0;width:100%;height:5px;background:var(--red)}
  .flyer--back .divider{top:320px}

  .headline{position:absolute;left:18px;top:312px;font-family:"Roboto Condensed",sans-serif;font-style:italic;font-weight:900;text-transform:uppercase;line-height:.9}
  .headline span{display:block}
  .headline__local{font-size:48px;color:var(--ink);padding-left:36px}
  .headline__trade{font-size:70px;color:var(--red)}
  .headline__experts{font-size:82px;color:var(--blue)}

  .section-title{font-family:"Roboto Condensed",sans-serif;font-style:italic;font-weight:700;text-decoration:underline;text-underline-offset:3px}
  .speciality{position:absolute;left:26px;top:506px}
  .speciality .section-title{color:var(--red);font-size:22px}
  .bullet-list{list-style:none;font-family:"Lato",sans-serif;color:var(--ink)}
  .speciality .bullet-list{font-size:14px;margin-top:4px}
  .speciality .bullet-list li::before{content:"•";color:var(--blue);margin-right:6px}

  .call-band{position:absolute;left:0;color:var(--white);font-family:"Roboto Condensed",sans-serif;font-style:italic;font-weight:700;padding-left:24px;display:flex;flex-direction:column;justify-content:center}
  .call-band__label{font-size:17px}
  .call-band__number{font-size:25px;display:flex;align-items:center;gap:6px}
  .call-band__number svg{width:16px;height:16px}
  .flyer--front .call-band{top:580px;width:100%;height:72px;background:linear-gradient(90deg,var(--blue-dark),var(--blue))}
  .flyer--back .call-band{top:628px;width:62%;height:76px;background:var(--red)}

  .payments{position:absolute;left:24px;display:flex;align-items:center;gap:22px}
  .flyer--front .payments{top:672px;gap:12px}
  .flyer--back .payments{top:716px}
  .payments svg{display:block}
  .payment-name{font-family:"Roboto Condensed",sans-serif;font-weight:800;font-size:22px;color:var(--navy);text-transform:uppercase;letter-spacing:1px}

  .illustration--relining{position:absolute;right:0;bottom:0;width:160px;height:190px;border-top:6px solid var(--red);border-left:6px solid var(--red);border-top-left-radius:160px 170px;background:linear-gradient(180deg,#4b8dbf 0%,#3f6b2b 35%,#5a3a1e 60%,#d07b1c 80%,#2a1a0c 100%)}

  .badge{position:absolute;left:50px;top:275px;width:96px;height:96px;border-radius:50%;background:var(--white);border:6px solid var(--red)}

  .services{position:absolute;left:20px;top:390px}
  .services .section-title{color:var(--blue);font-size:25px}
  .services .bullet-list{font-size:15.5px;margin-top:6px;line-height:1.45}
  .services .bullet-list li{display:flex;align-items:center;gap:8px}
  .services .bullet-list svg{width:8px;height:11px;flex:none}

  .photo--back-plumber{right:0;top:350px;width:175px;height:410px;background:linear-gradient(180deg,#eeeeee 0%,#e4c9b3 18%,#2f4fa8 40%,#1e3a8a 70%,#e0a33a 82%,#253f86 100%)}
</style>
</head>
<body>

<section class="flyer flyer--front" aria-label="Flyer front: drains and pipe relining">
  <header class="brand-band">
    <span class="brand-name">Harbourline</span>
    <span class="brand-sub">Plumbing &amp; Drainage</span>
  </header>

  <div class="photo photo--front-tradesman" role="img" aria-label="Photo of a plumber in a blue work shirt holding hoses, with a tool belt, in a kitchen"></div>

  <h1 class="headline">
    <span class="headline__local">Your Local</span>
    <span class="headline__trade">Plumbing</span>
    <span class="headline__experts">Experts</span>
  </h1>

  <div class="speciality">
    <h2 class="section-title">specialised in:</h2>
    <ul class="bullet-list">
      <li>Drains Cleaning</li>
      <li>Pipe Relining</li>
    </ul>
  </div>

  <div class="call-band">
    <span class="call-band__label">CALL US:</span>
    <span class="call-band__number">
      <svg viewBox="0 0 24 24" aria-hidden="true"><circle cx="12" cy="12" r="10.5" fill="none" stroke="#fff" stroke-width="2"/><path d="M8.5 7c.6-.6 1.4-.5 1.8.1l1 1.6c.3.5.2 1.1-.2 1.5l-.6.5c.5 1.1 1.3 2 2.4 2.6l.5-.6c.4-.4 1-.5 1.5-.2l1.6 1c.6.4.7 1.2.1 1.800l-.8.8c-.8.8-2.1.8-3.3.1-2.2-1.3-3.9-3.1-5-5.2-.6-1.2-.6-2.4.2-3.2z" fill="#fff"/></svg>
      0487 312 564
    </span>
  </div>

  <div class="payments" aria-label="Payment methods: cash, quon, cheque">
    <svg width="30" height="20" viewBox="0 0 30 20" aria-label="Cash"><rect x="5" y="1" width="24" height="12" rx="1" fill="#fff" stroke="#1b2f6b" stroke-width="1.5"/><rect x="1" y="6" width="24" height="12" rx="1" fill="#fff" stroke="#1b2f6b" stroke-width="1.5"/><circle cx="13" cy="12" r="3" fill="none" stroke="#1b2f6b" stroke-width="1.5"/></svg>
    <span class="payment-name">quon</span>
    <svg width="44" height="22" viewBox="0 0 44 22" aria-label="Cheque"><rect x="1" y="1" width="42" height="20" fill="#fff" stroke="#1b2f6b" stroke-width="1.5"/><rect x="1" y="1" width="42" height="4" fill="#2f7fd0"/><line x1="6" y1="11" x2="30" y2="11" stroke="#1b2f6b" stroke-width="1.2"/><line x1="6" y1="16" x2="24" y2="16" stroke="#1b2f6b" stroke-width="1.2"/></svg>
  </div>

  <div class="illustration--relining" role="img" aria-label="Illustration of a cut-away underground pipe with tree roots and a new liner being inserted"></div>
</section>

<section class="flyer flyer--back" aria-label="Flyer back: general plumbing services">
  <header class="brand-band">
    <span class="brand-name">Harbourline</span>
    <span class="brand-sub">Plumbing &amp; Drainage</span>
  </header>

  <div class="photo photo--back-pipework" role="img" aria-label="Close-up photo of a plumber tightening chrome pipework under a sink with a wrench"></div>
  <div class="divider"></div>

  <div class="badge" aria-hidden="true"></div>

  <div class="services">
    <h2 class="section-title">Other Services:</h2>
    <ul class="bullet-list">
      <li><svg viewBox="0 0 8 11" aria-hidden="true"><path d="M4 0C4 0 0 5 0 7.2A4 4 0 0 0 8 7.2C8 5 4 0 4 0z" fill="#e8333d"/></svg>General Plumbing.</li>
      <li><svg viewBox="0 0 8 11" aria-hidden="true"><path d="M4 0C4 0 0 5 0 7.2A4 4 0 0 0 8 7.2C8 5 4 0 4 0z" fill="#e8333d"/></svg>Eg leaking taps</li>
      <li><svg viewBox="0 0 8 11" aria-hidden="true"><path d="M4 0C4 0 0 5 0 7.2A4 4 0 0 0 8 7.2C8 5 4 0 4 0z" fill="#e8333d"/></svg>Leaking toilets</li>
      <li><svg viewBox="0 0 8 11" aria-hidden="true"><path d="M4 0C4 0 0 5 0 7.2A4 4 0 0 0 8 7.2C8 5 4 0 4 0z" fill="#e8333d"/></svg>Burst pipes</li>
      <li><svg viewBox="0 0 8 11" aria-hidden="true"><path d="M4 0C4 0 0 5 0 7.2A4 4 0 0 0 8 7.2C8 5 4 0 4 0z" fill="#e8333d"/></svg>Cctv inspections</li>
      <li><svg viewBox="0 0 8 11" aria-hidden="true"><path d="M4 0C4 0 0 5 0 7.2A4 4 0 0 0 8 7.2C8 5 4 0 4 0z" fill="#e8333d"/></svg>Gas installations</li>
      <li><svg viewBox="0 0 8 11" aria-hidden="true"><path d="M4 0C4 0 0 5 0 7.2A4 4 0 0 0 8 7.2C8 5 4 0 4 0z" fill="#e8333d"/></svg>Blocked drains.</li>
    </ul>
  </div>

  <div class="photo photo--back-plumber" role="img" aria-label="Photo of a smiling plumber in blue overalls with arms crossed, holding a pipe wrench and wearing a tool belt"></div>

  <div class="call-band">
    <span class="call-band__label">CALL US:</span>
    <span class="call-band__number">
      <svg viewBox="0 0 24 24" aria-hidden="true"><circle cx="12" cy="12" r="10.5" fill="none" stroke="#fff" stroke-width="2"/><path d="M8.5 7c.6-.6 1.4-.5 1.8.1l1 1.6c.3.5.2 1.1-.2 1.5l-.6.5c.5 1.1 1.3 2 2.4 2.6l.5-.6c.4-.4 1-.5 1.5-.2l1.6 1c.6.4.7 1.2.1 1.8l-.8.8c-.8.8-2.1.8-3.3.1-2.2-1.3-3.900-3.1-5-5.2-.6-1.2-.6-2.4.2-3.2z" fill="#fff"/></svg>
      0487 312 564
    </span>
  </div>

  <div class="payments" aria-label="Payment methods: cash, quon, cheque">
    <svg width="30" height="20" viewBox="0 0 30 20" aria-label="Cash"><rect x="5" y="1" width="24" height="12" rx="1" fill="#fff" stroke="#1b2f6b" stroke-width="1.5"/><rect x="1" y="6" width="24" height="12" rx="1" fill="#fff" stroke="#1b2f6b" stroke-width="1.5"/><circle cx="13" cy="12" r="3" fill="none" stroke="#1b2f6b" stroke-width="1.5"/></svg>
    <span class="payment-name">quon</span>
    <svg width="44" height="22" viewBox="0 0 44 22" aria-label="Cheque"><rect x="1" y="1" width="42" height="20" fill="#fff" stroke="#1b2f6b" stroke-width="1.5"/><rect x="1" y="1" width="42" height="4" fill="#2f7fd0"/><line x1="6" y1="11" x2="30" y2="11" stroke="#1b2f6b" stroke-width="1.2"/><line x1="6" y1="16" x2="24" y2="16" stroke="#1b2f6b" stroke-width="1.2"/></svg>
  </div>
</section>

</body>
</html>
```